Calloway Pizza - Takeout Menu Design

We are looking for a takeout menu design.
We are looking for a( 5" x 8.5" DOUBLE SIDED) flyer with our available pizza flavors
Must be easy to ready and not "busy"

Must include our logo (attached)
website: www.callowaypizza.example
address:
Tern Ridge Plaza
314, 418 9 Avenue SW
and the following details:
Visit our website for our complete appetizer, pasta, salad and catering menu.

Winner of this contest will also be offered to create a few print designs via artpoolhub.

Please do not hesitate to ask any questions.

Target Market(s)

Business / Office clientele

Industry/Entity Type

Pizza place / specializing in corporate orders

Requirements
Must have
• Easy to read
Should not have
• Can not be busy or cluttered

```html
<!DOCTYPE html>
<html lang="en">
<head>
<meta charset="utf-8">
<title>Calloway Pizza – Takeout Menu</title>
<link href="https://fonts.googleapis.com/css2?family=Bebas+Neue&family=Oswald:wght@500&family=Poppins:wght@300&family=Share+Tech&display=swap" rel="stylesheet">
<style>
  :root{
    --stage:#f39220;
    --board-top:#18191c;
    --board-mid:#1f2228;
    --board-low:#2b3244;
    --ink:#ffffff;
    --ink-soft:#a9abb0;
    --ink-dim:#8c8f96;
    --price-lg:#ffe600;
    --accent:#e3222b;
    --note:#2aa7e0;
    --crust:#c9772f;
    --cheese:#e9d9b8;
    --band-dark:rgba(150,15,20,.6);
    --band-bright:rgba(200,25,30,.88);
  }
  *{margin:0;padding:0;box-sizing:border-box}
  html,body{width:1200px;height:1041px;overflow:hidden;background:var(--stage)}
  .stage{position:relative;width:1200px;height:1041px}
  .menu-page{
    position:absolute;width:388px;height:660px;overflow:hidden;
    background:
      repeating-linear-gradient(90deg,rgba(255,255,255,.025) 0 1px,transparent 1px 5px),
      linear-gradient(180deg,var(--board-top) 0%,var(--board-mid) 55%,var(--board-low) 85%,#1d2230 100%);
    font-family:"Share Tech",sans-serif;color:var(--ink);
  }
  .page-front{left:153px;top:104px}
  .page-back{left:658px;top:277px}

  .brand{position:absolute;left:0;right:0;top:16px;text-align:center;white-space:nowrap;
    font-family:"Poppins",sans-serif;font-weight:300;font-size:32px;letter-spacing:1px;color:var(--ink)}
  .brand-mark{display:inline-block;width:22px;height:22px;border-radius:50%;background:var(--accent);
    vertical-align:middle;margin-right:8px;position:relative;top:-3px}
  .brand-ghost{top:8px;font-size:40px;letter-spacing:2px;color:rgba(255,255,255,.09)}

  .section-title{position:absolute;font-family:"Bebas Neue",sans-serif;font-size:25px;white-space:nowrap;
    color:var(--board-top);-webkit-text-stroke:.6px #d8d9dc;letter-spacing:.3px;line-height:1}
  .size-head{position:absolute;font-size:12px;display:flex}
  .size-head span{display:block;text-align:right}
  .size-head .lg{color:var(--price-lg)}

  .classic-list{position:absolute;left:53px;top:118px;width:286px;list-style:none}
  .classic-list li{display:flex;align-items:baseline;height:19.8px;font-size:14px;letter-spacing:1px;color:var(--ink-soft);white-space:nowrap}
  .classic-list .dots{flex:1;border-bottom:1px dotted var(--ink-dim);margin:0 4px;transform:translateY(-3px)}
  .classic-list .p8{width:52px;text-align:right;color:var(--ink)}
  .classic-list .p13{width:56px;text-align:right;color:var(--price-lg)}

  .spec-list{position:absolute;list-style:none}
  .spec-list li{display:grid;grid-template-columns:1fr auto auto;align-items:end}
  .spec-list .name{grid-column:1;grid-row:1;color:var(--ink);letter-spacing:1px;white-space:nowrap}
  .spec-list .desc{grid-column:1;grid-row:2;color:var(--ink-dim);letter-spacing:.6px;line-height:1.25}
  .spec-list .p8,.spec-list .p13{grid-row:2;text-align:right;white-space:nowrap}
  .spec-list .p8{grid-column:2;color:var(--ink)}
  .spec-list .p13{grid-column:3;color:var(--price-lg)}

  .front-spec{left:33px;top:341px;width:306px}
  .front-spec li{height:29.6px}
  .front-spec .name{font-size:12px}
  .front-spec .desc{font-size:9.5px}
  .front-spec .p8{width:48px;font-size:11px}
  .front-spec .p13{width:39px;font-size:11px}

  .back-spec{left:25px;top:72px;width:339px}
  .back-spec li{min-height:25.3px}
  .back-spec .name{font-size:11px}
  .back-spec .desc{font-size:6.6px;padding-right:6px}
  .back-spec .p8{width:48px;font-size:8.5px}
  .back-spec .p13{width:39px;font-size:8.5px}
  .back-spec .two-price{line-height:1.25}

  .tax-note{position:absolute;font-family:Arial,sans-serif;font-style:italic;font-size:6.5px;color:var(--note);white-space:nowrap}
  .tax-vertical{left:6px;top:620px;transform:rotate(-90deg);transform-origin:left top}
  .tax-flat{left:16px;top:572px}

  .pizza-photo{position:absolute;border-radius:50% 50% 0 0/100% 100% 0 0;
    background:radial-gradient(ellipse at 50% 40%,var(--cheese) 0%,#dcb27a 40%,var(--crust) 75%,#7a3a18 100%)}
  .front-photo{left:79px;top:579px;width:279px;height:90px}
  .back-photo{left:40px;top:575px;width:325px;height:95px}

  .info-band{position:absolute;left:0;right:0;top:628px;height:32px;
    background:linear-gradient(90deg,var(--band-dark),var(--band-bright),var(--band-dark));
    font-family:"Oswald",sans-serif;font-weight:500;font-size:10.5px;line-height:11.5px;
    text-align:center;color:var(--ink);padding-top:4px;text-transform:uppercase;white-space:nowrap}
  .contact-band{font-size:8.5px;line-height:9.5px;padding-top:2px}
  .contact-band .web{color:var(--price-lg)}
</style>
</head>
<body>
<div class="stage">

  <section class="menu-page page-front">
    <div class="brand"><span class="brand-mark"></span>CALLOWAY PIZZA</div>

    <h2 class="section-title" style="left:20px;top:82px">Classic Take-Out Pizza</h2>
    <div class="size-head" style="left:266px;top:98px"><span style="width:14px">8″</span><span class="lg" style="width:62px">13″</span></div>
    <ul class="classic-list">
      <li><span>PEPPERONI &amp; MUSHROOM</span><span class="dots"></span><span class="p8">$12.99</span><span class="p13">$30.95</span></li>
      <li><span>PEPPERONI</span><span class="dots"></span><span class="p8">$11.99</span><span class="p13">$29.95</span></li>
      <li><span>HAWAIIAN</span><span class="dots"></span><span class="p8">$12.99</span><span class="p13">$30.95</span></li>
      <li><span>BEEF &amp; MUSHROOM</span><span class="dots"></span><span class="p8">$13.49</span><span class="p13">$32.95</span></li>
      <li><span>PEPPERONI &amp; HAM</span><span class="dots"></span><span class="p8">$12.99</span><span class="p13">$30.95</span></li>
      <li><span>HAM &amp; MUSHROOM</span><span class="dots"></span><span class="p8">$12.99</span><span class="p13">$30.95</span></li>
      <li><span>BEEF &amp; ONION</span><span class="dots"></span><span class="p8">$13.49</span><span class="p13">$32.95</span></li>
      <li><span>CHEESE</span><span class="dots"></span><span class="p8">$11.99</span><span class="p13">$29.95</span></li>
    </ul>

    <h2 class="section-title" style="left:20px;top:307px">Speciality Take-Out Pizza</h2>
    <div class="size-head" style="left:288px;top:323px"><span style="width:12px">8″</span><span class="lg" style="width:38px">13″</span></div>
    <ul class="spec-list front-spec">
      <li><span class="name">ALL MEAT</span><span class="desc">PEPPERONI, BEEF &amp; SMOKED HAM &amp; BACON</span><span class="p8">$14.99</span><span class="p13">$35.95</span></li>
      <li><span class="name">DOUBLE PEPPERONI</span><span class="desc">LOADS OF PEPPERONI</span><span class="p8">$13.49</span><span class="p13">$32.95</span></li>
      <li><span class="name">HOT HONEY PEPPERONI</span><span class="desc">DOUBLE PEPPERONI AND DRIZZLED WITH HOT HONEY</span><span class="p8">$14.49</span><span class="p13">$34.95</span></li>
      <li><span class="name">HAWAIIAN HEAT</span><span class="desc">SMOKED HAM, PINEAPPLE AND BANANA PEPPERS</span><span class="p8">$13.49</span><span class="p13">$32.95</span></li>
      <li><span class="name">FOUR CHEESE</span><span class="desc">MOZZARELLA, FETA, ROMANO AND CHEDDAR CHEESE</span><span class="p8">$13.49</span><span class="p13">$32.95</span></li>
      <li><span class="name">MONTREAL</span><span class="desc">PEPPERONI &amp; DOUBLE SMOKED BACON</span><span class="p8">$13.49</span><span class="p13">$32.95</span></li>
      <li><span class="name">MONTREAL HEAT</span><span class="desc">PEPPERONI, DOUBLE SMOKED BACON<br>&amp; BANANA PEPPERS</span><span class="p8" style="align-self:start">$13.99</span><span class="p13" style="align-self:start">$33.95</span></li>
    </ul>

    <p class="tax-note tax-vertical">*All prices are exclusive of GST.</p>
    <div class="pizza-photo front-photo" role="img" aria-label="Photo of a baked cheese pizza"></div>
    <p class="info-band">All of our pizzas are prepared fresh everyday using only<br>the finest mozzarella blend and ingredients.</p>
  </section>

  <section class="menu-page page-back">
    <div class="brand brand-ghost">CALLOWAY PIZZA</div>
    <h2 class="section-title" style="left:21px;top:44px">Speciality Take-Out Pizza</h2>
    <div class="size-head" style="left:300px;top:64px"><span style="width:12px">8″</span><span class="lg" style="width:40px">13″</span></div>
    <ul class="spec-list back-spec">
      <li><span class="name">SUPREME</span><span class="desc">PEPPERONI, MUSHROOMS &amp; GREEN PEPPERS</span><span class="p8">$13.49</span><span class="p13">$32.95</span></li>
      <li><span class="name">CANADIAN</span><span class="desc">PEPPERONI, MUSHROOMS &amp; HAM</span><span class="p8">$13.49</span><span class="p13">$32.95</span></li>
      <li><span class="name">BBQ CHICKEN</span><span class="desc">CHICKEN BREAST, HICKORY BBQ SAUCE &amp; RED ONIONS.</span><span class="p8">$13.99</span><span class="p13">$33.95</span></li>
      <li><span class="name">BBQ CHICKEN PLUS</span><span class="desc">CHICKEN BREAST, HICKORY BBQ SAUCE, RED ONIONS &amp; CILANTRO</span><span class="p8">$14.79</span><span class="p13">$34.95</span></li>
      <li><span class="name">SPICY BBQ CHICKEN</span><span class="desc">CHICKEN BREAST, HICKORY BBQ SAUCE, RED ONIONS &amp; BANANA PEPPERS</span><span class="p8">$14.49</span><span class="p13">$35.95</span></li>
      <li><span class="name">SWEET CHILI CHICKEN</span><span class="desc">CHICKEN BREAST, PINEAPPLE, RED ONIONS &amp; SWEET CHILI SAUCE</span><span class="p8">$14.49</span><span class="p13">$35.95</span></li>
      <li><span class="name">CHICKEN CLUB</span><span class="desc">CHICKEN BREAST, DOUBLE SMOKED BACON, RED ONIONS AND TOMATOES</span><span class="p8">$14.79</span><span class="p13">$35.95</span></li>
      <li><span class="name">ATHENEAN</span><span class="desc">CHICKEN BREAST, SPINACH, FETA CHEESE AND TOMATO</span><span class="p8">$14.49</span><span class="p13">$34.95</span></li>
      <li><span class="name">GREEK SUPREME</span><span class="desc" style="white-space:nowrap">CHICKEN BREAST, FETA CHEESE, TOMATO, GREEN PEPPER, RED ONIONS &amp; BLACK OLIVES</span><span class="p8">$14.99</span><span class="p13">$35.95</span></li>
      <li><span class="name">MEDITERRANEAN CHICKEN</span><span class="desc">SEASONED CHICKEN BREAST, TOMATOES, RED ONIONS AND FETA CHEESE</span><span class="p8">$14.79</span><span class="p13">$35.95</span></li>
      <li><span class="name">ORIGINAL SPINACH</span><span class="desc">SPINACH &amp; FETA CHEESE</span><span class="p8">$13.49</span><span class="p13">$32.95</span></li>
      <li><span class="name">ZEUS</span><span class="desc">SPINACH, FETA CHEESE AND TOMATOES</span><span class="p8">$13.95</span><span class="p13">$33.95</span></li>
      <li><span class="name">GREEK</span><span class="desc">FETA CHEESE, TOMATO, GREEN PEPPERS, RED ONIONS AND BLACK OLIVES</span><span class="p8">$13.99</span><span class="p13">$33.95</span></li>
      <li><span class="name">VEGETARIAN</span><span class="desc">MUSHROOMS, TOMATOES, GREEN PEPPERS AND BLACK OLIVES</span><span class="p8">$13.49</span><span class="p13">$32.95</span></li>
      <li><span class="name">VEGGIE DELIGHT</span><span class="desc">MUSHROOMS, TOMATOES, GREEN PEPPERS, BLACK OLIVES &amp; ONION</span><span class="p8">$13.95</span><span class="p13">$33.95</span></li>
      <li><span class="name">DELUXE</span><span class="desc">PEPPERONI, MUSHROOMS, HAM, TOMATOES, GREEN PEPPERS AND RED ONIONS</span><span class="p8">$14.49</span><span class="p13">$34.95</span></li>
      <li><span class="name">CALLOWAY SPECIAL</span><span class="desc">PEPPERONI, MUSHROOMS, HAM, GREEN PEPPERS AND BLACK OLIVES</span><span class="p8">$14.49</span><span class="p13">$34.95</span></li>
      <li><span class="name">DILL PICKLE</span><span class="desc">CRISPY DILL PICKLES, FRESH DILL WITH OUR CREAM BASED GARLIC SAUCE.<br>SERVED WITH/WITHOUT BACON.</span><span class="p8 two-price">$13.49<br>$14.49</span><span class="p13 two-price">$32.95<br>$35.95</span></li>
      <li><span class="name">BBQ PULLED PORK</span><span class="desc">PULLED PORK, RED ONIONS, RED PEPPERS AND CILANTRO.</span><span class="p8">$14.49</span><span class="p13">$35.95</span></li>
    </ul>
    <p class="tax-note tax-flat">*All prices are exclusive of GST.</p>
    <div class="pizza-photo back-photo" role="img" aria-label="Photo of a baked cheese pizza with olives"></div>
    <div class="info-band contact-band">
      <p>Visit our website for our complete appetizer, pasta, salad and catering menu</p>
      <p><span class="web">www.callowaypizza.example</span> · Tern Ridge Plaza · 314, 418 9 Avenue SW</p>
    </div>
  </section>

</div>
</body>
</html>
```